Soy Candle Business needs a label design

We need a label design for a new company selling soy candles - Velvet Hearth Studio.

We are using apothecary jars in 3 sizes.
As per attached candles will be dressed with a beautiful black bow and all finished with a diamante in centre of bow.

We would like label done on lid of candle jars - 5cm circle (5cm from one side to the other), this way one label will fit each product size. Label will be done as a sticker.

We are thinking of the background colour to be black, however are open to recommendations. We want label to be classy, elegant and simple.

Inspiration for candle design came from attached invitation that features the bow, and beautiful vintage paper on top area.

Label should include the following 3 pieces of information:
Velvet Hearth Studio (company name)
Coconut Lime (this will change depending on fragrance)
Soy Candle

Velvet Hearth Studio does not have a company logo... what is done for the label will set tone for what is done across other elements of business moving forward.

Industry/Entity Type

Business

Requirements
Must have
• Velvet Hearth Studio
Fragrance Flavour
Soy Candle

```html
<!DOCTYPE html>
<html lang="en">
<head>
<meta charset="UTF-8">
<title>Velvet Hearth Studio – Coconut Lime Soy Candle Label</title>
<link rel="stylesheet" href="https://fonts.googleapis.com/css2?family=Macondo&family=Fira+Sans+Condensed:wght@400;700&display=swap">
<style>
  :root {
    --page: #ffffff;
    --label-black: #000000;
    --label-white: #ffffff;
    --pattern-dark: #1a1a1a;
    --pattern-light: #5a5a5a;
  }
  html, body {
    margin: 0;
    padding: 0;
    width: 1200px;
    height: 900px;
    overflow: hidden;
    background: var(--page);
  }
  .canvas {
    position: relative;
    width: 1200px;
    height: 900px;
  }
  .label-shape {
    position: absolute;
    inset: 0;
  }
  .label-text {
    position: absolute;
    left: 0;
    width: 1200px;
    margin: 0;
    text-align: center;
    color: var(--label-white);
    white-space: nowrap;
    line-height: 1;
  }
  .brand-name {
    font-family: "Macondo", cursive;
    font-weight: 400;
    font-size: 96px;
  }
  .brand-name--line1 { top: 222px; }
  .brand-name--line2 { top: 322px; }
  .fragrance {
    top: 500px;
    font-family: "Fira Sans Condensed", sans-serif;
    font-weight: 700;
    font-size: 72px;
    letter-spacing: 0.5px;
  }
  .product-type {
    top: 598px;
    font-family: "Fira Sans Condensed", sans-serif;
    font-weight: 400;
    font-size: 68px;
    letter-spacing: 1px;
  }
</style>
</head>
<body>
  <main class="canvas">
    <svg class="label-shape" width="1200" height="900" viewBox="0 0 1200 900" xmlns="http://www.w3.org/2000/svg">
      <defs>
        <clipPath id="label-circle">
          <circle cx="600" cy="444" r="380"/>
        </clipPath>
        <linearGradient id="flourish-tone" x1="0" y1="0" x2="1" y2="1">
          <stop offset="0" stop-color="var(--pattern-dark)"/>
          <stop offset="0.5" stop-color="var(--pattern-light)"/>
          <stop offset="1" stop-color="var(--pattern-dark)"/>
        </linearGradient>
      </defs>
      <circle class="label-base" cx="600" cy="444" r="380" fill="var(--label-black)"/>
      <g clip-path="url(#label-circle)">
        <rect class="flourish-band flourish-band--top" x="200" y="60" width="800" height="124"
              fill="url(#flourish-tone)" role="img"
              aria-label="Vintage white scrollwork flourish pattern on black"/>
        <rect class="band-rule" x="200" y="184" width="800" height="5" fill="var(--label-white)"/>
        <rect class="band-rule" x="200" y="688" width="800" height="5" fill="var(--label-white)"/>
        <rect class="flourish-band flourish-band--bottom" x="200" y="693" width="800" height="140"
              fill="url(#flourish-tone)" role="img"
              aria-label="Vintage white scrollwork flourish pattern on black"/>
      </g>
    </svg>

    <p class="label-text brand-name brand-name--line1">Velvet Hearth</p>
    <p class="label-text brand-name brand-name--line2">Studio</p>
    <p class="label-text fragrance">COCONUT LIME</p>
    <p class="label-text product-type">SOY CANDLE</p>
  </main>
</body>
</html>
```